Event Flyer with matching Ticket

I need and flyer (2 sided) and Ticket (2 sided- same info on both sides)
Templates are attached for each item

Flyer and tickets need to have an abstract art jazz theme

The back of the flyer can just have the name of the event "Vunter Presents Autumn Evening of Grace Ft The Brass Moonlighters with the date and time"

Vunter Presents Autumn Evening of Grace Ft The Brass Moonlighters

Date June 9th 7-11 Doors open at 6:30
$35 -$ 40 at the door
VIP tables $350
hor dourves and Sprits available

Pick up tickets at Pine Hollow Medical Clinic 4183 N Larkmoor St Tulsa Ok 74130
Or purchase tickets on line at Seatquill (need to get the Address)

Vunter Address 4207 North Larkmoor Street, Tulsa, OK (maybe include a map)

Ticket info-
Sample ticket attached

Same basic layout the the sample ticket attached.

Font styles to use
Script

Requirements
Must have
• abstract art jazz theme background
• Nice looking fonts nothing so fancy its hard to read
Nice to have
• Location map

```html
<!DOCTYPE html>
<html lang="en">
<head>
<meta charset="utf-8">
<title>Vunter Presents Autumn Evening of Grace</title>
<link rel="stylesheet" href="https://fonts.googleapis.com/css2?family=Great+Vibes&family=Oswald:wght@500&family=Lato:ital,wght@0,300;0,400;1,300;1,700&display=swap">
<style>
  :root {
    --paper: #ffffff;
    --lavender: #9e9bb1;
    --lavender-shadow: #8a8491;
    --ink: #1c1b20;
    --box-dark: #2f2d31;
    --corner: #0f1316;
    --white: #ffffff;
    --rule: #4a4852;
  }
  * { margin: 0; padding: 0; box-sizing: border-box; }
  html, body { width: 1200px; height: 754px; overflow: hidden; background: var(--paper); }
  .canvas { position: relative; width: 1200px; height: 754px; }

  .side { position: absolute; top: 0; height: 754px; background: var(--lavender); overflow: hidden; }
  .side--front { left: 0; width: 590px; }
  .side--back { left: 607px; width: 593px; }

  .artwork {
    position: absolute; inset: 0;
    background:
      radial-gradient(ellipse 42% 55% at 62% 48%, var(--lavender-shadow) 0%, rgba(138,132,145,0.55) 55%, rgba(158,155,177,0) 100%),
      radial-gradient(ellipse 30% 40% at 40% 78%, rgba(125,120,137,0.6) 0%, rgba(158,155,177,0) 100%);
  }

  .front-presents {
    position: absolute; top: 62px; left: 0; width: 100%; text-align: center;
    font-family: "Oswald", sans-serif; font-weight: 500; font-size: 31px;
    color: var(--white); letter-spacing: 0.5px;
  }
  .rule { position: absolute; left: 50px; width: 490px; height: 1px; background: var(--rule); }
  .rule--short { left: 78px; width: 436px; }
  .front-title {
    position: absolute; top: 205px; left: 0; width: 100%; text-align: center;
    font-family: "Great Vibes", cursive; font-weight: 400; font-size: 60px; line-height: 62px; color: var(--ink);
  }
  .front-featuring {
    position: absolute; top: 448px; left: 0; width: 100%; text-align: center;
    font-family: "Oswald", sans-serif; font-weight: 500; font-size: 25px; color: var(--white);
  }
  .front-band {
    position: absolute; top: 494px; left: 0; width: 100%; text-align: center;
    font-family: "Great Vibes", cursive; font-size: 42px; color: var(--ink);
  }
  .corner { position: absolute; left: 0; top: 562px; width: 192px; height: 192px; }
  .corner-date {
    position: absolute; left: 38px; top: 616px; width: 160px; height: 28px; line-height: 28px;
    text-align: center; transform: rotate(45deg); transform-origin: center center;
    font-family: "Lato", sans-serif; font-weight: 300; font-size: 23px; color: var(--white);
    white-space: nowrap;
  }

  .header-box {
    position: absolute; left: 76px; top: 32px; width: 448px; height: 155px;
    background: var(--box-dark); border: 1px solid #d9d7df;
    text-align: center; color: var(--white); font-family: "Lato", sans-serif; font-weight: 300;
  }
  .header-presents { margin-top: 13px; font-size: 22px; line-height: 28px; }
  .header-title { margin-top: 8px; font-family: "Great Vibes", cursive; font-weight: 400; font-size: 33px; line-height: 42px; }
  .header-feat { margin-top: 10px; font-size: 20px; line-height: 26px; }

  .details-box {
    position: absolute; left: 119px; top: 212px; width: 358px; height: 158px;
    border: 1px solid var(--white); padding: 4px;
  }
  .details-inner {
    width: 100%; height: 100%; border: 1px solid var(--white);
    text-align: center; color: var(--white); font-family: "Lato", sans-serif; font-weight: 300;
    font-size: 18px; line-height: 33px; padding-top: 9px;
  }

  .pickup {
    position: absolute; left: 0; width: 100%; text-align: center;
    font-family: "Lato", sans-serif; font-size: 13px; color: var(--ink);
  }
  .pickup strong { font-weight: 700; font-style: italic; }

  .location-box {
    position: absolute; left: 61px; top: 493px; width: 472px; height: 228px;
    border: 1px solid var(--white); padding: 4px;
  }
  .location-inner { position: relative; width: 100%; height: 100%; border: 1px solid var(--white); }
  .location-address {
    margin-top: 12px; text-align: center;
    font-family: "Lato", sans-serif; font-style: italic; font-weight: 300; font-size: 17px; color: var(--white);
  }
  .location-map {
    position: absolute; left: 120px; top: 48px; width: 240px; height: 150px;
    background: rgba(120,116,132,0.55); border-radius: 4px;
  }
</style>
</head>
<body>
<main class="canvas">

  <section class="side side--front">
    <div class="artwork" role="img" aria-label="Toned photograph of a musician playing an upright double bass"></div>
    <p class="front-presents">VUNTER PRESENTS</p>
    <div class="rule" style="top:173px"></div>
    <div class="rule rule--short" style="top:190px"></div>
    <h1 class="front-title">Autumn Evening of<br>Grace</h1>
    <div class="rule" style="top:360px"></div>
    <div class="rule rule--short" style="top:376px"></div>
    <p class="front-featuring">FEATURING</p>
    <p class="front-band">The Brass Moonlighters</p>
    <svg class="corner" viewBox="0 0 192 192" aria-hidden="true">
      <polygon points="0,0 192,0 192,192" fill="var(--corner)"/>
      <polygon points="0,0 0,192 192,192" fill="var(--paper)"/>
    </svg>
    <p class="corner-date">June 9th 7-11</p>
  </section>

  <section class="side side--back">
    <div class="artwork" role="img" aria-label="Toned photograph of a musician playing an upright double bass"></div>
    <header class="header-box">
      <p class="header-presents">Vunter Presents</p>
      <h2 class="header-title">Autumn Evening of Grace</h2>
      <p class="header-feat">Ft The Brass Moonlighters</p>
    </header>
    <div class="details-box">
      <div class="details-inner">
        <p>June 9th, 2015, 7 pm - 11 pm</p>
        <p>Doors open at 6:30</p>
        <p>$35 -$ 40 at the door / VIP tables $350</p>
        <p>hor dourves and Sprits available</p>
      </div>
    </div>
    <p class="pickup" style="top:390px"><strong>Pick up tickets at</strong> Pine Hollow Medical Clinic 4183 N Larkmoor St, Tulsa, Ok - 74130</p>
    <p class="pickup" style="top:423px">Or purchase tickets on line at Seatquill:</p>
    <p class="pickup" style="top:456px">www.seatquill.com/event</p>
    <div class="location-box">
      <div class="location-inner">
        <p class="location-address">Address 4207 North Larkmoor Street, Tulsa, OK</p>
        <div class="location-map" role="img" aria-label="Street map of the venue surroundings with a pin marking the venue"></div>
      </div>
    </div>
  </section>

</main>
</body>
</html>
```